Harlow Crest Holdings (Remodeling company) needs a logo and business card

We need a business card design for a new company. We "flip" upmarket houses (buy, remodel and sell) in the Austin, TX area. I'd like neutral colors (grey, white, gold black). I would like it to include a simple, clean logo. Our designs are modern and uncluttered and I would like that reflected in the business card design.

Target Market(s)

Young professionals, Families, Retirees. Our properties will sell for $750k+

Industry/Entity Type

Real Estate

Contact Information for Business Card

Harlow Crets Holdings
Mona Harlow
(979) 555 0142
Owner
Rolf Tandem
(512) 555 0176
Realtor

Logo Text

Harlow Crest Holdings

Font styles to use
Serif
Script

Requirements
Must have
• Simple, classic design
Nice to have
• Clean lines, modern look
Should not have
• Too traditionally

```html
<!DOCTYPE html>
<html lang="en">
<head>
<meta charset="utf-8">
<title>Harlow Crest Holdings – Business Card</title>
<link rel="stylesheet" href="https://fonts.googleapis.com/css2?family=Noto+Serif:wght@700&display=swap">
<style>
  :root {
    --page-bg: #ffffff;
    --card-dark: #221c1a;
    --card-gold: #fdc82f;
    --card-stripe: #3a3533;
    --ink: #231f1c;
  }
  html, body {
    margin: 0;
    padding: 0;
    width: 1200px;
    height: 999px;
    overflow: hidden;
    background: var(--page-bg);
  }
  .business-card {
    position: absolute;
    left: 237px;
    top: 291px;
    width: 727px;
    height: 415px;
    background: var(--card-dark);
    overflow: hidden;
  }
  .card-sweep {
    position: absolute;
    inset: 0;
    width: 727px;
    height: 415px;
  }
  .brand {
    position: absolute;
    left: 26px;
    top: 22px;
    display: flex;
    align-items: center;
    gap: 16px;
  }
  .brand-circle {
    width: 62px;
    height: 62px;
    border: 8px solid var(--card-gold);
    border-radius: 50%;
    box-sizing: border-box;
  }
  .brand-name {
    font-family: "Noto Serif", serif;
    font-weight: 700;
    font-size: 22px;
    line-height: 1.15;
    color: var(--card-gold);
    width: 130px;
  }
  .contact {
    position: absolute;
    right: 45px;
    top: 255px;
    text-align: right;
    font-family: "Noto Serif", serif;
    font-weight: 700;
    color: var(--ink);
  }
  .contact-name {
    margin: 0;
    font-size: 45px;
    line-height: 1.1;
    letter-spacing: 0.3px;
  }
  .contact-phone {
    margin: 4px 0 0;
    font-size: 22px;
    line-height: 1.2;
  }
</style>
</head>
<body>
  <div class="business-card">
    <svg class="card-sweep" viewBox="0 0 727 415" aria-hidden="true">
      <path fill="var(--card-stripe)" d="M727 56 C492 59 288 196 229 415 L247 415 C300 200 500 65 727 60 Z"/>
      <path fill="var(--card-gold)" d="M727 60 C500 65 300 200 247 415 L727 415 Z"/>
    </svg>

    <div class="brand">
      <div class="brand-circle"></div>
      <div class="brand-name">Harlow Crest Holdings</div>
    </div>

    <div class="contact">
      <p class="contact-name">Rolf Tandem</p>
      <p class="contact-phone">(512) 555 0176</p>
    </div>
  </div>
</body>
</html>
```